Emmy award winning Hollywood sound studio needs a cool website

We need a website designed and coded to showcase our company and talent to our current and future clients. We are a post-production sound studio that works with Brambletoon, Vidora, Calder Sisters, Glimmerforge, and other major Hollywood studios and companies. We primarily work designing sound effects for animated TV shows like Puddlefin McGee, Rookie Rangers Roll!, Tiger Dojo: Lantern Riders, Fossil Valley Stampede Files, The Sly Crew, My Aunt the Starship Pilot, Spear of Helix, and the recent Vidora movie Wren and the Quiet. A website for our company would provide basic information about our studio and services, the kinds of projects we are currently working on and have worked on in the past, the awards we have won or been nominated for, and most importantly showcase our talented engineers so that producers and directors can get to know the people they might want to collaborate with. Our studio is located in Burbank, CA right in the heart of where all the studios are located. We have a basic company logo. We don't really have a color scheme to our studio so we're very open and flexible in that department. We have decorated our studio with a bit of an Art Deco style to invoke an old classy movie theater from the golden age of Hollywood. Our lobby resembles the lobby of a movie theater complete with a neon marquee where we post fun sayings or quotes from our shows. I think it would be fun for the website design to reflect that Art Deco/classic movie theater feeling. Another website that I think has a good simple design for inspiration is Fernhollow Audio: "www.fernaudio.example".
Target Market(s)
Major Hollywood Studios, Animation production companies, independent film/TV production
Industry/Entity Type
Hollywood, Television, Streaming, Entertainment, Games
Coding
Coded - Design and coding required
Number of Pages Required
5+ page
Look and feel

```html
<!DOCTYPE html>
<html lang="en">
<head>
<meta charset="utf-8">
<title>Echo Marquee — Our Services</title>
<link rel="stylesheet" href="https://fonts.googleapis.com/css2?family=Lexend:wght@400;500;600&family=Figtree:wght@400;500;600;700&display=swap">
<style>
:root{
  --ink:#14151d;
  --card:#1b1f30;
  --card-line:#3b3f55;
  --gold:#d2a645;
  --gold-deep:#b98a2c;
  --white:#ffffff;
  --muted:#b9bccb;
  --grey:#777a86;
  --line:#e3e4e8;
  --text:#1c1d24;
}
*{margin:0;padding:0;box-sizing:border-box}
html,body{width:1200px;height:3509px;overflow:hidden}
body{font-family:"Figtree",sans-serif;color:var(--text);background:var(--ink);position:relative}
.abs{position:absolute}
.display{font-family:"Lexend",sans-serif;font-weight:500;letter-spacing:-0.5px}

/* hero */
.hero{position:absolute;left:0;top:0;width:1200px;height:428px;
  background:radial-gradient(ellipse at 70% 30%,#3b3a44 0%,#24232b 45%,#121218 100%)}
.hero-photo{position:absolute;inset:0;background:linear-gradient(160deg,rgba(80,74,70,.55),rgba(20,20,26,.2) 60%,rgba(60,42,28,.5))}
.logo{position:absolute;left:75px;top:44px;display:flex;align-items:center;gap:10px;color:var(--white);font-family:"Lexend",sans-serif;font-weight:600;font-size:23px}
.logo-mark{width:16px;height:16px;background:var(--gold)}
.nav{position:absolute;left:440px;top:52px;display:flex;gap:24px;font-weight:600;font-size:15px;color:var(--white)}
.nav .active{border-bottom:2px solid var(--white);padding-bottom:6px}
.tools{position:absolute;left:1018px;top:50px;display:flex;gap:26px}
.hero-title{position:absolute;left:0;width:1200px;top:220px;text-align:center;color:var(--white);font-size:49px}
.crumb{position:absolute;left:0;width:1200px;top:305px;text-align:center;color:var(--white);font-size:11px;font-weight:700;letter-spacing:1px}

/* services */
.services{position:absolute;left:0;top:428px;width:1200px;height:655px;background:
  radial-gradient(circle at 0% 0%,rgba(190,145,50,.5) 0%,rgba(110,80,30,.22) 22%,rgba(20,21,29,0) 42%),var(--ink)}
.eyebrow{font-size:11px;font-weight:700;letter-spacing:1.2px;text-transform:uppercase}
.circle-btn{position:absolute;width:50px;height:50px;border-radius:50%;background:var(--gold);display:flex;align-items:center;justify-content:center}
.card{position:absolute;top:223px;width:304px;height:343px;background:var(--card);border:1px solid var(--card-line);padding:50px 31px 0}
.card h3{font-family:"Lexend",sans-serif;font-weight:500;font-size:21px;color:var(--white);margin-top:38px;white-space:nowrap}
.card p{font-size:13.5px;line-height:23px;color:var(--muted);margin-top:14px;width:240px}
.card .go{margin-top:18px}

/* works */
.light{position:absolute;left:0;top:1083px;width:1200px;height:1329px;background:var(--white)}
.works-title{position:absolute;left:117px;top:80px;font-size:41px;color:var(--text)}
.shot{position:absolute;top:162px;height:330px}
.dots{position:absolute;display:flex;gap:7px}
.dots i{display:block;width:7px;height:7px;background:var(--text)}
.dots i.on{background:var(--gold)}
.award{position:absolute;top:632px;width:110px;height:36px;border-radius:4px;background:#cfc9bb}
.booth{position:absolute;left:117px;top:757px;width:470px;height:484px;background:linear-gradient(135deg,#d8cdb6,#a4906c 45%,#5f4a34 75%,#c6b290)}
.player{position:absolute;left:613px;top:757px;width:470px;height:195px;border:2px solid var(--line);padding:34px 34px 0}
.player h4{font-family:"Lexend",sans-serif;font-weight:500;font-size:22px}
.player .artist{color:var(--grey);font-size:14px;margin-top:8px}
.tracks{position:absolute;left:613px;top:982px;width:470px;font-size:14px}
.track{display:flex;justify-content:space-between;height:57px;align-items:center;border-bottom:1px solid var(--line)}
.track:last-child{border-bottom:none}
.track b{font-weight:700}
.track span.by{color:var(--grey)}
.track.now,.track.now span.by{color:var(--gold-deep)}

/* testimonials & footer */
.talk{position:absolute;left:0;top:2412px;width:1200px;height:1097px;background:
  radial-gradient(circle at 100% 100%,rgba(190,145,50,.42) 0%,rgba(20,21,29,0) 28%),var(--ink);color:var(--white)}
.center{position:absolute;left:0;width:1200px;text-align:center}
.quote{position:absolute;left:260px;width:680px;top:328px;text-align:center;font-size:17px;line-height:28px;color:#e8e9ef}
.rule{position:absolute;left:117px;top:651px;width:966px;height:1px;background:#2c2e3a}
.social{position:absolute;left:117px;top:733px;display:flex;gap:30px;font-family:"Lexend",sans-serif;font-size:17px}
.cta{position:absolute;left:117px;top:822px;font-size:39px;line-height:46px}
.cta a{color:var(--gold)}
.copy{position:absolute;left:117px;top:981px;font-size:13px;color:#9a9cab}
.copy b{color:var(--white);font-weight:500}
</style>
</head>
<body>

<header class="hero">
  <div class="hero-photo" role="img" aria-label="Sound engineer with headphones at a large mixing console in a dim studio"></div>
  <div class="logo"><span class="logo-mark"></span>Echo Marquee</div>
  <nav class="nav"><span>Home</span><span class="active">Pages</span><span>Blog</span><span>Shop</span><span>Contacts</span></nav>
  <div class="tools">
    <svg width="22" height="24" viewBox="0 0 22 24" fill="none" stroke="#fff" stroke-width="2"><path d="M3 7h14l-1 15H4z"/><path d="M7 7V5a3 3 0 0 1 6 0v2"/><circle cx="17" cy="19" r="4" fill="#d2a645" stroke="none"/></svg>
    <svg width="22" height="22" viewBox="0 0 22 22" fill="none" stroke="#fff" stroke-width="2"><circle cx="9" cy="9" r="7"/><path d="M14 14l6 6"/></svg>
    <svg width="20" height="20" viewBox="0 0 20 20" fill="#fff"><circle cx="3" cy="3" r="2"/><circle cx="10" cy="3" r="2"/><circle cx="17" cy="3" r="2"/><circle cx="3" cy="10" r="2"/><circle cx="10" cy="10" r="2"/><circle cx="17" cy="10" r="2"/><circle cx="3" cy="17" r="2"/><circle cx="10" cy="17" r="2"/><circle cx="17" cy="17" r="2"/></svg>
  </div>
  <h1 class="hero-title display">Our Services</h1>
  <div class="crumb">HOME / OUR SERVICES</div>
</header>

<section class="services">
  <div class="eyebrow abs" style="left:117px;top:88px;color:#fff">Sound for Animation</div>
  <h2 class="display abs" style="left:117px;top:110px;font-size:41px;color:#fff">Our Services</h2>
  <p class="abs" style="left:439px;top:122px;width:440px;font-size:14px;line-height:24px;color:var(--muted)">From the first spotting session to the final mix, our Burbank team builds every boing, whoosh and roar your series needs, on time and on budget.</p>
  <div class="circle-btn" style="left:973px;top:120px"><svg width="18" height="14" viewBox="0 0 18 14" fill="none" stroke="#fff" stroke-width="2"><path d="M17 7H2M7 1L1 7l6 6"/></svg></div>
  <div class="circle-btn" style="left:1031px;top:120px"><svg width="18" height="14" viewBox="0 0 18 14" fill="none" stroke="#fff" stroke-width="2"><path d="M1 7h15M11 1l6 6-6 6"/></svg></div>

  <article class="card" style="left:117px">
    <svg width="60" height="60" viewBox="0 0 60 60" fill="none"><path d="M4 30h8l14-14v28L12 30" fill="#d2a645"/><path d="M34 20a14 14 0 0 1 0 20M42 12a24 24 0 0 1 0 36" stroke="#d2a645" stroke-width="4"/></svg>
    <h3>Sound Effects Design</h3>
    <p>Custom effects for every gag, chase and creature, built to the beat of the cut.</p>
    <svg class="go" width="16" height="12" viewBox="0 0 16 12" fill="none" stroke="#fff" stroke-width="1.6"><path d="M0 6h14M9 1l5 5-5 5"/></svg>
  </article>
  <article class="card" style="left:448px">
    <svg width="60" height="60" viewBox="0 0 60 60"><rect x="2" y="2" width="56" height="56" rx="6" fill="#d2a645"/><g stroke="#14151d" stroke-width="3"><path d="M15 12v36M30 12v36M45 12v36"/></g><g fill="#14151d"><rect x="10" y="20" width="10" height="6"/><rect x="25" y="34" width="10" height="6"/><rect x="40" y="24" width="10" height="6"/></g></svg>
    <h3>Re-recording Mix</h3>
    <p>Final stereo and surround mixes delivered to every network and streaming spec.</p>
    <svg class="go" width="16" height="12" viewBox="0 0 16 12" fill="none" stroke="#fff" stroke-width="1.6"><path d="M0 6h14M9 1l5 5-5 5"/></svg>
  </article>
  <article class="card" style="left:778px">
    <svg width="60" height="60" viewBox="0 0 60 60"><rect x="20" y="2" width="20" height="34" rx="10" fill="#d2a645"/><path d="M10 28a20 20 0 0 0 40 0M30 48v10M18 58h24" stroke="#d2a645" stroke-width="4" fill="none"/></svg>
    <h3>Foley Recording</h3>
    <p>Footsteps, props and cloth performed live on our own stage by seasoned artists.</p>
    <svg class="go" width="16" height="12" viewBox="0 0 16 12" fill="none" stroke="#fff" stroke-width="1.6"><path d="M0 6h14M9 1l5 5-5 5"/></svg>
  </article>
  <article class="card" style="left:1110px">
    <svg width="60" height="60" viewBox="0 0 60 60"><rect x="2" y="8" width="44" height="30" rx="3" fill="#d2a645"/><path d="M10 46l8-8h10z" fill="#d2a645"/><g fill="#14151d"><rect x="10" y="17" width="28" height="4"/><rect x="10" y="25" width="18" height="4"/></g></svg>
    <h3>ADR &amp; Dialogue</h3>
    <p>Voice sessions and dialogue edits for cast anywhere in the world.</p>
    <svg class="go" width="16" height="12" viewBox="0 0 16 12" fill="none" stroke="#fff" stroke-width="1.6"><path d="M0 6h14M9 1l5 5-5 5"/></svg>
  </article>
</section>

<section class="light">
  <h2 class="works-title display">Our Best Works</h2>
  <div class="shot" style="left:0;width:281px;background:linear-gradient(120deg,#f0e4c8,#d9b46a 55%,#3f7fb8)" role="img" aria-label="Still from the animated series Puddlefin McGee"></div>
  <div class="shot" style="left:306px;width:587px;background:radial-gradient(circle at 45% 45%,#e4a03a,#a8412a 45%,#1c1c24 85%)" role="img" aria-label="Still from the animated film Wren and the Quiet"></div>
  <div class="shot" style="left:919px;width:281px;background:linear-gradient(135deg,#56709a,#2a3247 50%,#3c8f4a 80%,#c2702c)" role="img" aria-label="Still from the animated series Fossil Valley Stampede Files"></div>
  <div class="dots" style="left:575px;top:536px"><i></i><i class="on"></i><i></i><i></i></div>

  <div class="award" style="left:181px" aria-label="Award badge"></div>
  <div class="award" style="left:424px" aria-label="Award badge"></div>
  <div class="award" style="left:665px" aria-label="Award badge"></div>
  <div class="award" style="left:908px" aria-label="Award badge"></div>

  <div class="booth" role="img" aria-label="Foley stage with props and shoes laid out for recording"></div>

  <div class="player">
    <h4>“Puddlefin McGee”</h4>
    <div class="artist">Milo Harker, Sound Designer</div>
    <svg class="abs" style="left:34px;top:114px" width="400" height="40" viewBox="0 0 400 40" fill="none">
      <circle cx="19" cy="20" r="17" stroke="#1c1d24" stroke-width="2"/><path d="M15 13l10 7-10 7z" fill="#1c1d24"/>
      <text x="50" y="25" font-family="Figtree,sans-serif" font-size="12" fill="#1c1d24">00:00</text>
      <rect x="104" y="19" width="140" height="2" fill="#d5d6db"/>
      <text x="260" y="25" font-family="Figtree,sans-serif" font-size="12" fill="#1c1d24">00:00</text>
      <path d="M318 16h5l6-5v18l-6-5h-5z" fill="#1c1d24"/><path d="M333 15a6 6 0 0 1 0 10" stroke="#1c1d24" stroke-width="1.5"/>
      <rect x="350" y="19" width="44" height="3" fill="#1c1d24"/>
    </svg>
  </div>

  <div class="tracks">
    <div class="track now"><span><b>1. “Puddlefin McGee”</b> <span class="by">— Milo Harker</span></span><b>0:16</b></div>
    <div class="track"><span><b>2. “The Sly Crew”</b> <span class="by">— Tess Alvarado</span></span><b>0:11</b></div>
    <div class="track"><span><b>3. “Spear of Helix”</b> <span class="by">— Dean Whitlock</span></span><b>0:11</b></div>
    <div class="track"><span><b>4. “Rookie Rangers Roll!”</b> <span class="by">— Rhea Castellan</span></span><b>0:11</b></div>
    <div class="track"><span><b>5. “Wren and the Quiet”</b> <span class="by">— Otis Fairbanks</span></span><b>0:10</b></div>
  </div>
</section>

<section class="talk">
  <div class="center eyebrow" style="top:88px">They Talk About Us</div>
  <h2 class="center display" style="top:110px;font-size:40px">The Best Studio in Burbank</h2>
  <div class="abs" style="left:555px;top:191px;width:90px;height:90px;border-radius:50%;background:radial-gradient(circle at 50% 40%,#c9a15a,#6b4f2a)" role="img" aria-label="Portrait of the reviewer"></div>
  <p class="quote">Every episode comes back sounding bigger than we imagined. The team treats each gag like a movie moment, and their engineers are a joy to work with in the room.</p>
  <div class="circle-btn" style="left:117px;top:337px"><svg width="18" height="14" viewBox="0 0 18 14" fill="none" stroke="#fff" stroke-width="2"><path d="M17 7H2M7 1L1 7l6 6"/></svg></div>
  <div class="circle-btn" style="left:1033px;top:337px"><svg width="18" height="14" viewBox="0 0 18 14" fill="none" stroke="#fff" stroke-width="2"><path d="M1 7h15M11 1l6 6-6 6"/></svg></div>
  <svg class="abs" style="left:586px;top:432px" width="28" height="24" viewBox="0 0 28 24" fill="#d2a645"><path d="M0 24V12C0 5 4 1 11 0l1 3C8 4 6 7 6 11h6v13zM16 24V12c0-7 4-11 11-12l1 3c-4 1-6 4-6 8h6v13z"/></svg>
  <div class="center" style="top:480px;font-family:Lexend,sans-serif;font-weight:600;font-size:16px">Marisol Quinn</div>
  <div class="center" style="top:509px;font-size:13px;color:var(--muted)">Producer, Brambletoon</div>
  <div class="dots" style="left:572px;top:568px"><i class="on"></i><i style="background:#fff"></i><i style="background:#fff"></i></div>
  <div class="rule"></div>
  <div class="social"><span>Friendloop</span><span>Chirpline</span><span>Pixelcourt</span><span>Snapgrove</span></div>
  <div class="cta display">Let's work together!<br>Just drop us a line - <a href="mailto:hello@echomarquee.example">hello@echomarquee.example</a></div>
  <div class="copy"><b>Echo Marquee</b> © 2024. All Rights Reserved.</div>
  <div class="circle-btn" style="left:1132px;top:1038px;width:38px;height:38px"><svg width="12" height="16" viewBox="0 0 12 16" fill="none" stroke="#fff" stroke-width="2"><path d="M6 15V2M1 7l5-5 5 5"/></svg></div>
</section>

</body>
</html>
```